LTCG Prospectus to invite exhibitors to annual conference

We need a 2 page front and back design for an association who is preparing for their annual conference and are inviting exhibitors to attend the meeting for the first time ever. Attached is the content that needs to be inserted into the flyer. Key details include:
+ Learning Text and Courseware Guild
+ Meeting Dates - February 2-5, 2016
+ Location - Marlow Sagebrush Ridge Lodge in Tucson, Arizona
Please refer to http://quillandslate.org/ for color branding, I've uploaded the association's logo for use.
The final design should include both the written content and graphics to show the demographic data of the association's members.
Target Market(s)
Professional - Targeting companies that service the needs of educational publishers in the book markets (think brightwell, penrow tillis, ashby dunmore kestrel, etc.).
Look and feel
Each slider illustrates characteristics of the customer's brand and the style your logo design should communicate.

```html
<!DOCTYPE html>
<html lang="en">
<head>
<meta charset="utf-8">
<title>LTCG Prospectus – Member Demographics</title>
<link href="https://fonts.googleapis.com/css2?family=Open+Sans:wght@400;600;700&display=swap" rel="stylesheet">
<style>
  :root{
    --page:#ffffff;
    --ink:#222222;
    --navy:#1f3a5f;
    --blue:#5b9bd5;
    --orange:#ed7d31;
    --grey:#a5a5a5;
    --gold:#ffc000;
    --deep-blue:#4472c4;
    --green:#70ad47;
    --band-top:#d9d9d9;
    --band-bottom:#ffffff;
    --frame:#d0d0d0;
    --muted:#7f7f7f;
  }
  *{box-sizing:border-box;margin:0;padding:0}
  html,body{width:849px;height:1200px;overflow:hidden;background:var(--page)}
  body{font-family:"Open Sans",Arial,sans-serif;color:var(--ink);position:relative}
  .abs{position:absolute}
  .chart-frame{border:1px solid var(--frame);background:var(--page)}
  .chart-frame svg{display:block;width:100%;height:100%}
  .member-counts{left:125px;top:200px;font-size:15px;line-height:20px}
  .shelf-band{left:0;width:849px;height:58px;
    background:linear-gradient(to bottom,var(--band-top) 0%,#efefef 45%,var(--band-bottom) 100%);
    box-shadow:inset 0 6px 8px -4px rgba(0,0,0,.25)}
  .shelf-band h2{position:absolute;top:14px;font-size:17px;font-weight:700;color:var(--navy);white-space:nowrap}
  .title-list{list-style:none;font-size:15px;line-height:23px}
  .brand{left:92px;top:1012px;display:flex;align-items:center;gap:10px}
  .brand-mark{width:46px;height:46px;border-radius:50%;background:var(--blue)}
  .brand-name{font-size:19px;font-weight:700;color:var(--muted);line-height:22px;width:240px}
  .floor{left:0;bottom:0;width:849px;height:150px;background:linear-gradient(to bottom,#ffffff,#e4e4e4)}
  .books{left:595px;top:935px;width:230px;height:265px;
    background:linear-gradient(to bottom,#d8dde3,#8f9aa6)}
</style>
</head>
<body>

<div class="floor abs"></div>

<!-- Member composition pie -->
<div class="chart-frame abs" style="left:113px;top:28px;width:255px;height:158px">
  <svg viewBox="0 0 255 158">
    <text x="127" y="16" font-size="8" text-anchor="middle" fill="#595959">Member Composition</text>
    <rect x="70" y="24" width="6" height="6" fill="var(--blue)"/><text x="79" y="30" font-size="7" fill="#595959">Publishers</text>
    <rect x="135" y="24" width="6" height="6" fill="var(--orange)"/><text x="144" y="30" font-size="7" fill="#595959">Wholesalers</text>
    <g transform="translate(127,92) rotate(-90)">
      <circle r="28" fill="none" stroke="var(--blue)" stroke-width="56" stroke-dasharray="123.5 176" />
      <circle r="28" fill="none" stroke="var(--orange)" stroke-width="56" stroke-dasharray="0 123.5 52.5 176" />
    </g>
  </svg>
</div>

<!-- Annual meeting attendees bars -->
<div class="chart-frame abs" style="left:425px;top:28px;width:340px;height:172px">
  <svg viewBox="0 0 340 172">
    <text x="170" y="16" font-size="8" text-anchor="middle" fill="#595959">Annual Meeting Attendees</text>
    <line x1="30" y1="145" x2="320" y2="145" stroke="#d9d9d9"/>
    <rect x="60" y="45" width="22" height="100" fill="var(--blue)"/>
    <rect x="86" y="100" width="22" height="45" fill="var(--orange)"/>
    <rect x="155" y="38" width="22" height="107" fill="var(--blue)"/>
    <rect x="181" y="98" width="22" height="47" fill="var(--orange)"/>
    <rect x="250" y="40" width="22" height="105" fill="var(--blue)"/>
    <rect x="276" y="100" width="22" height="45" fill="var(--orange)"/>
    <text x="84" y="156" font-size="7" text-anchor="middle" fill="#595959">2013</text>
    <text x="179" y="156" font-size="7" text-anchor="middle" fill="#595959">2014</text>
    <text x="274" y="156" font-size="7" text-anchor="middle" fill="#595959">2015</text>
    <rect x="120" y="162" width="5" height="5" fill="var(--blue)"/><text x="128" y="167" font-size="6" fill="#595959">Publishers</text>
    <rect x="175" y="162" width="5" height="5" fill="var(--orange)"/><text x="183" y="167" font-size="6" fill="#595959">Wholesalers</text>
  </svg>
</div>

<p class="member-counts abs">Publisher Member Companies: 82<br>Wholesaler Member Companies: 35</p>

<section class="shelf-band abs" style="top:238px">
  <h2 style="left:113px">2014 2015 Member Composition</h2>
  <h2 style="left:480px">Number of Annual Meeting Attendees</h2>
</section>

<!-- Publisher titles pie -->
<div class="chart-frame abs" style="left:155px;top:325px;width:270px;height:200px">
  <svg viewBox="0 0 270 200">
    <text x="135" y="16" font-size="8" text-anchor="middle" fill="#595959">Publisher Attendee Job Titles</text>
    <g transform="translate(95,110) rotate(-90)">
      <circle r="33" fill="none" stroke="var(--green)" stroke-width="66" stroke-dasharray="207 208"/>
      <circle r="33" fill="none" stroke="var(--orange)" stroke-width="66" stroke-dasharray="0 84 45 208"/>
      <circle r="33" fill="none" stroke="var(--grey)" stroke-width="66" stroke-dasharray="0 129 24 208"/>
      <circle r="33" fill="none" stroke="var(--gold)" stroke-width="66" stroke-dasharray="0 153 30 208"/>
      <circle r="33" fill="none" stroke="var(--deep-blue)" stroke-width="66" stroke-dasharray="0 183 25 208"/>
    </g>
    <g font-size="6" fill="#595959">
      <rect x="178" y="82" width="5" height="5" fill="var(--green)"/><text x="186" y="87">Vice President</text>
      <rect x="178" y="92" width="5" height="5" fill="var(--orange)"/><text x="186" y="97">Sales Manager</text>
      <rect x="178" y="102" width="5" height="5" fill="var(--grey)"/><text x="186" y="107">President</text>
      <rect x="178" y="112" width="5" height="5" fill="var(--gold)"/><text x="186" y="117">Sales Director</text>
      <rect x="178" y="122" width="5" height="5" fill="var(--deep-blue)"/><text x="186" y="127">Accounts Manager</text>
    </g>
  </svg>
</div>

<ol class="title-list abs" style="left:481px;top:352px">
  <li>1. Vice President (22)</li>
  <li>2. Sales Manager 18</li>
  <li>3. President, CEO or Owner (16)</li>
  <li>4. Sales Director (16)</li>
  <li>5. Accounts Manager (9)</li>
</ol>

<section class="shelf-band abs" style="top:566px">
  <h2 style="left:113px">Top 5 Publisher Attendee Job Titles</h2>
</section>

<!-- Wholesaler titles pie -->
<div class="chart-frame abs" style="left:155px;top:652px;width:270px;height:198px">
  <svg viewBox="0 0 270 198">
    <text x="135" y="16" font-size="8" text-anchor="middle" fill="#595959">Wholesaler Attendee Job Titles</text>
    <g transform="translate(95,108) rotate(-90)">
      <circle r="33" fill="none" stroke="var(--blue)" stroke-width="66" stroke-dasharray="207 208"/>
      <circle r="33" fill="none" stroke="var(--orange)" stroke-width="66" stroke-dasharray="0 77 36 208"/>
      <circle r="33" fill="none" stroke="var(--grey)" stroke-width="66" stroke-dasharray="0 113 27 208"/>
      <circle r="33" fill="none" stroke="var(--gold)" stroke-width="66" stroke-dasharray="0 140 68 208"/>
    </g>
    <g font-size="6" fill="#595959">
      <rect x="178" y="86" width="5" height="5" fill="var(--blue)"/><text x="186" y="91">President</text>
      <rect x="178" y="96" width="5" height="5" fill="var(--orange)"/><text x="186" y="101">Vice President</text>
      <rect x="178" y="106" width="5" height="5" fill="var(--grey)"/><text x="186" y="111">Collection Development</text>
      <rect x="178" y="116" width="5" height="5" fill="var(--gold)"/><text x="186" y="121">General Manager</text>
    </g>
  </svg>
</div>

<ol class="title-list abs" style="left:481px;top:680px">
  <li>1. President, CEO or Owner (17)</li>
  <li>2. Vice President (8)</li>
  <li>3. Collection Development (6)</li>
  <li>4. Director of General Manager (15)</li>
</ol>

<section class="shelf-band abs" style="top:864px">
  <h2 style="left:113px">Top 5 Wholesaler Attendee Job Titles</h2>
</section>

<div class="brand abs">
  <span class="brand-mark"></span>
  <span class="brand-name">Learning Text and Courseware Guild</span>
</div>

<div class="books abs" role="img" aria-label="Stack of books beside a tablet showing a page"></div>

</body>
</html>
```